Plakat-Design für IT-Systemhaus
brisk IT Solutions suchte ein neues Design in der Kategorie Plakate und hat ein Projekt auf grafikwerkhof.de gestartet.
brisk IT Solutions
The winner of our first design contests on this site. Can only say positive things about them. They work fast, respond in a timely manner and created a great design for us. Overall we're very happy with Quillwick.
Zielgruppe
Wir sind ein IT-Systemhaus mit dem Fokus auf individuelle Cloud Lösungen inkl. bester Kundenbetreuung.
Unsere primäre Zielgruppe sind Unterhnemenskunden, sprich das B2B Geschäft.
Aus der Gruppe der Unternehmenskunden interessieren uns besonders kleine und mittelständische Unternehmen.
Unser Corporate Design ist modern und dennoch auffällig gehalten.
Unsere bevorzugt Schriftart ist 'Ubuntu' bzw. 'Ubuntu Light'.
Unsere Grundfarben sind Orange (#ff8303) Grau (#747474).
Als orientierungshilfe haben wir unser Vorlage für Blöcke und Flyer mit angehangen.
Aufgabenstellung
Es handelt sich um eine Geländerwerbung (doppelseitig) zwischen einer Tankstelle und einer Straße gelegen. (Siehe Anhang)
Die Maße des Anzeitgetafel sind wie folgt: Querformat 135 x 65 (breite x höhe)
Gerne würden wir auf eine etwas provokantere Fragestellung zurückgreifen, um Aufmerksamkeit zu eregen.
Gleichzeitig möchten wir als Lösungsfinder der Fragestellung wargenommen werden.
Gut gefallen hat uns diese Lösung: https://www.grafikwerkhof.at/527190-plakat-fuer-it-systemhaus
Des Weiteren sollte die Anzeige unser Logo, Webadresse sowie unsere Telefonnummer enthalten.
Für Kreative Vorschläge sind wir dankbar.

```html
<!DOCTYPE html>
<html lang="de">
<head>
<meta charset="utf-8">
<title>brisk IT Solutions – Geländerwerbung</title>
<link href="https://fonts.googleapis.com/css2?family=Ubuntu:wght@300;400;500;700&display=swap" rel="stylesheet">
<style>
  :root {
    --orange: #ff8303;
    --grey: #747474;
    --grey-dark: #3c3c3c;
    --stage: #efefef;
    --white: #ffffff;
  }
  * { margin: 0; padding: 0; box-sizing: border-box; }
  html, body { width: 1200px; height: 658px; overflow: hidden; background: var(--stage); }
  body { font-family: 'Ubuntu', sans-serif; position: relative; }

  .banner {
    position: absolute; left: 20px; top: 50px;
    width: 1160px; height: 558px; overflow: hidden;
    background: radial-gradient(ellipse at 40% 35%, #d4d4d4 0%, #a9a9a9 60%, #8e8e8e 100%);
  }
  .decor { position: absolute; inset: 0; }

  .cloud-art {
    position: absolute; left: 100px; top: 50px; width: 200px; height: 240px;
    border-radius: 100px 100px 20px 20px;
    background: linear-gradient(180deg, var(--orange) 0%, #f7a64f 55%, rgba(255,131,3,0.15) 100%);
  }

  .web-pill {
    position: absolute; left: 40px; top: 260px; width: 46px; height: 260px;
    border-radius: 23px; background: var(--orange);
    display: flex; align-items: center; justify-content: center;
  }
  .web-pill span {
    transform: rotate(-90deg); white-space: nowrap;
    color: var(--white); font-weight: 500; font-size: 20px;
  }

  .headline {
    position: absolute; left: 410px; top: 52px;
    color: var(--orange); font-weight: 500; font-size: 66px; line-height: 1.02;
  }
  .headline .quote { font-size: 52px; font-weight: 700; }
  .headline .line2 { padding-left: 12px; }

  .subline {
    position: absolute; left: 480px; top: 250px;
    color: var(--grey-dark); font-weight: 400; font-size: 38px; line-height: 1.12;
  }

  .services {
    position: absolute; left: 310px; top: 300px; list-style: none;
    color: var(--grey-dark); font-size: 15px; font-weight: 400;
  }
  .services li { display: flex; align-items: center; gap: 8px; margin-bottom: 18px; white-space: nowrap; }
  .services svg { width: 22px; height: 22px; flex: none; }

  .brand {
    position: absolute; left: 690px; top: 392px;
    color: var(--orange); font-weight: 400; font-size: 34px; letter-spacing: 0.5px;
  }

  .contact-band {
    position: absolute; left: 560px; right: 0; bottom: 30px; height: 30px;
    background: var(--orange); border-radius: 15px 0 0 15px;
    display: flex; align-items: center; padding-left: 36px;
    color: var(--white); font-size: 16px; font-weight: 500;
  }
</style>
</head>
<body>
<main class="banner">
  <svg class="decor" viewBox="0 0 1160 558" aria-hidden="true">
    <g fill="none" stroke="var(--orange)" stroke-width="3">
      <path d="M300 110 C340 100 370 98 402 104"/>
      <path d="M1060 20 C1020 60 1010 110 1060 150 C1100 180 1160 160 1160 120"/>
      <path d="M600 360 C610 395 640 415 680 420"/>
      <path d="M1000 558 L1000 470 A50 50 0 0 1 1100 470 L1100 558"/>
    </g>
    <g fill="var(--white)" opacity="0.85">
      <path d="M0 558 L0 330 A45 45 0 0 1 90 330 L90 558 Z"/>
      <path d="M1020 558 L1020 470 A45 45 0 0 1 1110 470 L1110 558 Z"/>
    </g>
    <g fill="none" stroke="var(--white)" stroke-width="2" opacity="0.8">
      <path d="M290 330 C270 360 255 420 280 480"/>
      <path d="M940 558 C930 500 950 450 990 430"/>
    </g>
  </svg>

  <div class="cloud-art" role="img" aria-label="Orange Wolke, aus der Netzwerkkabel nach unten hängen"></div>

  <div class="web-pill"><span>brisk-it.de</span></div>

  <h1 class="headline">
    <span class="quote">»</span> Wer hat wem<br>
    <span class="line2">was geCloud?<span class="quote">«</span></span>
  </h1>

  <p class="subline">Alles Neuland für Sie?<br>Wir erklären es Ihnen!</p>

  <ul class="services">
    <li><svg viewBox="0 0 26 26" fill="none" stroke="var(--grey-dark)" stroke-width="1.6"><rect x="3" y="4" width="20" height="7" rx="1"/><rect x="3" y="15" width="20" height="7" rx="1"/><circle cx="7" cy="7.5" r="1"/><circle cx="7" cy="18.5" r="1"/></svg>IT Infrastruktur</li>
    <li><svg viewBox="0 0 26 26" fill="none" stroke="var(--grey-dark)" stroke-width="1.6"><path d="M13 3 L21 6 V13 C21 18 17 21 13 23 C9 21 5 18 5 13 V6 Z"/><path d="M9 13 L12 16 L17 10"/></svg>IT Sicherheit</li>
    <li><svg viewBox="0 0 26 26" fill="none" stroke="var(--grey-dark)" stroke-width="1.6"><circle cx="9" cy="8" r="3.5"/><circle cx="18" cy="8" r="3.5"/><path d="M3 22 C3 16 15 16 15 22"/><path d="M12 22 C12 16 24 16 24 22"/></svg>IT Beratung</li>
    <li><svg viewBox="0 0 26 26" fill="none" stroke="var(--grey-dark)" stroke-width="1.6"><rect x="3" y="5" width="20" height="13" rx="1"/><path d="M9 22 H17 M13 18 V22"/></svg>IT Support</li>
  </ul>

  <div class="brand">brisk IT Solutions</div>

  <div class="contact-band">Lindenstraße 12 · 57000 Musterdorf · Tel.: +49 2700 / 12 34 56 0</div>
</main>
</body>
</html>
```